creating professional text layers for Varnello Product listings images

I need some text added to several images in a professional eye catching way. The text should be legible on desktop and mobile devices. Rough mocks will be provided. You will just need to make them pop and professional. There are 10 images required in total to the selected designer. Below are just 3 of them

```html
<!DOCTYPE html>
<html lang="en">
<head>
<meta charset="utf-8">
<title>Varnello New Banner</title>
<link href="https://fonts.googleapis.com/css2?family=Barlow+Condensed:wght@500&family=Bebas+Neue&family=Kaushan+Script&family=Montserrat:wght@500;800;900&display=swap" rel="stylesheet">
<style>
:root{
  --stage:#575757;
  --ink:#0b0b0b;
  --red:#e3121b;
  --red-deep:#a50b10;
  --white:#ffffff;
}
*{margin:0;padding:0;box-sizing:border-box}
html,body{width:1200px;height:426px;overflow:hidden;background:var(--stage)}
.canvas{position:relative;width:1200px;height:426px;background:var(--stage)}
.side-label{
  position:absolute;left:37px;top:216px;
  transform:translate(-50%,-50%) rotate(-90deg);
  font-family:"Montserrat",sans-serif;font-weight:800;font-size:21px;
  letter-spacing:4.2px;color:var(--white);white-space:nowrap;
}
.tile{position:absolute;top:30px;width:361px;height:361px;
  background:linear-gradient(135deg,#141414 0%,#1c1c1c 35%,var(--red-deep) 70%,var(--red) 88%);
  box-shadow:0 3px 8px rgba(0,0,0,.45)}
.tile-inner{position:absolute;overflow:hidden;background:var(--ink)}
.tile--speed .tile-inner{left:2px;top:2px;right:8px;bottom:8px}
.tile--payback{background:var(--red)}
.tile--payback .tile-inner{left:8px;top:8px;right:8px;bottom:8px}
.photo{position:absolute}
.headline{position:absolute;color:var(--white);white-space:nowrap;line-height:1}
.question-box{position:absolute;left:0;top:0;width:100%;height:100%}
.question{position:absolute;text-align:right;white-space:nowrap;
  font-family:"Barlow Condensed","Arial Narrow",sans-serif;font-weight:500;
  font-size:28px;line-height:26px;color:var(--white)}

/* tile 1 */
#tile-a{left:72px}
#tile-a .photo{left:0;top:0;width:220px;height:351px;
  background:radial-gradient(ellipse at 40% 45%,#cfcac0 0%,#8d8a85 35%,#2a2a2a 70%,var(--ink) 100%)}
#tile-a .headline{right:10px;font-family:"Bebas Neue",sans-serif;text-align:right}
#tile-a .h-variable{top:21px;font-size:43px}
#tile-a .h-speed{top:55px;font-size:63px;color:var(--red)}
#tile-a .h-control{top:108px;font-size:37px}
#tile-a .question{right:20px;top:168px}

/* tile 2 */
#tile-b{left:444px}
#tile-b .photo{inset:0;
  background:linear-gradient(180deg,#161616 0%,#2a2a2a 55%,#a8825e 78%,#c9a57e 100%),#222}
#tile-b .photo::after{content:"";position:absolute;left:170px;top:40px;width:140px;height:290px;
  background:linear-gradient(90deg,#7d828a,#a5aab1 50%,#6f747b);opacity:.85}
#tile-b .headline{left:13px;font-family:"Bebas Neue",sans-serif}
#tile-b .h-pays{top:22px;font-size:46px}
#tile-b .h-itself{top:56px;font-size:70px}
#tile-b .h-fast{top:102px;left:18px;font-family:"Kaushan Script",cursive;font-size:66px;color:var(--red);transform:rotate(-6deg)}

/* tile 3 */
#tile-c{left:811px}
#tile-c .photo{inset:0;
  background:radial-gradient(ellipse at 30% 50%,#d8cdb0 0%,#8f8a7f 30%,#2c3038 62%,#14161b 100%)}
#tile-c .headline{right:12px;font-family:"Montserrat",sans-serif;text-align:right}
#tile-c .h-variable{top:23px;font-size:36px;font-weight:900}
#tile-c .h-speed{top:55px;font-size:55px;font-weight:900;color:var(--red);letter-spacing:-1px}
#tile-c .h-control{top:109px;font-size:32px;font-weight:500;letter-spacing:3px;
  color:transparent;-webkit-text-stroke:1.3px var(--white)}
#tile-c .question{right:26px;top:168px}
</style>
</head>
<body>
<div class="canvas">
  <div class="side-label">VARNELLO NEW BANNER</div>

  <section class="tile tile--speed" id="tile-a">
    <div class="tile-inner">
      <div class="photo" role="img" aria-label="Wire stripping machine with speed dial, emergency stop and hand wheel"></div>
      <div class="headline h-variable">VARIABLE</div>
      <div class="headline h-speed">SPEED</div>
      <div class="headline h-control">CONTROL</div>
      <svg class="question-box" viewBox="0 0 351 351" aria-hidden="true">
        <polyline points="208,154 341,154 341,335 75,335" fill="none" stroke="#e3121b" stroke-width="1.5"/>
      </svg>
      <p class="question">How<br>Could You<br>Possibly<br>Strip All<br>Gauges At The<br>Same Speed?</p>
    </div>
  </section>

  <section class="tile tile--payback" id="tile-b">
    <div class="tile-inner">
      <div class="photo" role="img" aria-label="Man standing at a workbench beside the stripping machine and scrap copper wire"></div>
      <div class="headline h-pays">PAYS FOR</div>
      <div class="headline h-itself">ITSELF</div>
      <div class="headline h-fast">Fast</div>
    </div>
  </section>

  <section class="tile tile--speed" id="tile-c">
    <div class="tile-inner">
      <div class="photo" role="img" aria-label="Close view of the machine control box with speed dial, emergency stop and switch"></div>
      <div class="headline h-variable">VARIABLE</div>
      <div class="headline h-speed">SPEED</div>
      <div class="headline h-control">CONTROL</div>
      <svg class="question-box" viewBox="0 0 351 351" aria-hidden="true">
        <polyline points="153,154 338,154 338,334 128,334" fill="none" stroke="#e3121b" stroke-width="1.5"/>
      </svg>
      <p class="question">How<br>Could You<br>Possibly<br>Strip All<br>Gauges At The<br>Same Speed?</p>
    </div>
  </section>
</div>
</body>
</html>
```